Ad for Cyber Security Company- Print Ad

We are looking for an awesome designer to create a one page advertisement for the Brimox Security data analytics platform that will be featured in an upcoming security magazine. This is also going to be featured in an upcoming trade show. Brimox Security produced the BRIMOX platform to help companies unify their security environment and help them address Insider Threat, Fraud and Anomaly ID and resolution. BRIMOX uses an an advanced ingestion engine, machine learning, and workflow automation to ensure the right people are getting the right info at the right time. We serve enterprise level customers, augmenting and enhancing, not replacing their existing security stack. We would like few or single image, clean, and open ad built around the tagline 'Make Security a Team Sport.' We would like the logo to be featured, and include our website address on the page (www.brimoxsecurity.net). See below for style guide.

Target Market(s)

Industry insiders, Chief Information Security Officers (CISO) and Technical directors.

Other font styles liked:
• See style guide, but we are open to suggestion.

Requirements
Must have
• A single image (minimum), Feature the provided logo, Include the tagline 'Make Security a Team Sport' and have the website somewhere on the ad. The image should focus on the conveying the message of "Make Security a Team Sport" and not be a generic security (padlock, network, etc.) image.
• See included style guide.

```html
<!DOCTYPE html>
<html lang="en">
<head>
<meta charset="utf-8">
<title>Brimox Security – Make Security a Team Sport</title>
<link rel="stylesheet" href="https://fonts.googleapis.com/css2?family=Orbitron:wght@600;700&family=Ubuntu:wght@500&family=Open+Sans:wght@400;700&display=swap">
<style>
  :root {
    --orange: #f26522;
    --hero-light: #d9601f;
    --hero-mid: #b04616;
    --hero-dark: #5e2510;
    --charcoal: #2f2f31;
    --stripe-gray: #5d5d5f;
    --logo-gray: #3b3b3d;
    --white: #ffffff;
  }
  html, body {
    margin: 0;
    padding: 0;
    width: 960px;
    height: 1200px;
    overflow: hidden;
    background: var(--charcoal);
  }
  .ad {
    position: relative;
    width: 960px;
    height: 1200px;
    overflow: hidden;
    background: var(--charcoal);
  }
  .hero-photo {
    position: absolute;
    left: 0;
    top: 0;
    width: 960px;
    height: 813px;
    background:
      radial-gradient(ellipse 420px 320px at 58% 52%, rgba(60,22,8,0.75) 0%, rgba(60,22,8,0) 100%),
      linear-gradient(180deg, var(--hero-light) 0%, var(--hero-mid) 55%, var(--hero-dark) 100%);
  }
  .header-shapes {
    position: absolute;
    left: 0;
    top: 0;
  }
  .brand-mark {
    position: absolute;
    left: 180px;
    top: 52px;
    width: 68px;
    height: 68px;
    background: var(--orange);
  }
  .brand-name {
    position: absolute;
    left: 263px;
    top: 50px;
    margin: 0;
    font-family: 'Orbitron', sans-serif;
    font-weight: 700;
    font-size: 42px;
    line-height: 37px;
    letter-spacing: 1px;
    color: var(--logo-gray);
  }
  .tagline {
    position: absolute;
    left: 0;
    width: 960px;
    top: 594px;
    margin: 0;
    text-align: center;
    font-family: 'Orbitron', sans-serif;
    font-weight: 700;
    font-size: 61px;
    line-height: 62px;
    letter-spacing: 5px;
    color: var(--white);
    text-transform: uppercase;
  }
  .features-band {
    position: absolute;
    left: 0;
    top: 813px;
    width: 960px;
    height: 387px;
    background: var(--charcoal);
  }
  .notch {
    position: absolute;
    left: 464px;
    top: 813px;
  }
  .features {
    position: absolute;
    left: 0;
    top: 873px;
    width: 960px;
    margin: 0;
    padding: 0;
    list-style: none;
  }
  .feature {
    position: absolute;
    top: 0;
    width: 300px;
    text-align: center;
  }
  .feature-icon {
    display: block;
    margin: 0 auto;
    width: 90px;
    height: 90px;
  }
  .feature-label {
    margin-top: 25px;
    font-family: 'Ubuntu', sans-serif;
    font-weight: 500;
    font-size: 25px;
    line-height: 30px;
    color: var(--white);
    white-space: nowrap;
  }
  .feature-rule {
    width: 34px;
    height: 4px;
    margin: 12px auto 0;
    background: var(--orange);
    border-radius: 2px;
  }
  .feature--anomaly { left: 79px; }
  .feature--insider { left: 325px; }
  .feature--activity { left: 590px; }
  .social {
    position: absolute;
    left: 0;
    top: 1116px;
    display: flex;
    align-items: center;
  }
  .social-rule {
    width: 98px;
    height: 1px;
    background: var(--orange);
    margin-right: 18px;
  }
  .social-dot {
    width: 44px;
    height: 44px;
    border-radius: 50%;
    margin-right: 20px;
  }
  .social-dot--one { background: #3b5998; }
  .social-dot--two { background: #0e76a8; }
  .footer-shapes {
    position: absolute;
    left: 0;
    top: 1080px;
  }
  .web-address {
    position: absolute;
    right: 73px;
    top: 1124px;
    margin: 0;
    font-family: 'Open Sans', sans-serif;
    font-weight: 400;
    font-size: 33px;
    line-height: 46px;
    letter-spacing: 2.5px;
    color: var(--white);
  }
  .web-address strong { font-weight: 700; }
</style>
</head>
<body>
<main class="ad">

  <div class="hero-photo" role="img" aria-label="Aerial photo of a team of skydivers holding hands in a star formation over farmland, tinted orange"></div>

  <svg class="header-shapes" width="960" height="200" viewBox="0 0 960 200" aria-hidden="true">
    <polygon points="0,0 960,0 960,27 647,27 550,173 0,173" fill="var(--white)"/>
    <polygon points="647,27 677,27 585,148 557,148" fill="var(--stripe-gray)"/>
  </svg>

  <span class="brand-mark"></span>
  <p class="brand-name">BRIMOX<br>SECURITY</p>

  <h1 class="tagline">Make Security a<br>Team Sport</h1>

  <section class="features-band"></section>

  <svg class="notch" width="32" height="16" viewBox="0 0 32 16" aria-hidden="true">
    <polygon points="0,0 32,0 16,14" fill="var(--hero-dark)"/>
  </svg>

  <ul class="features">
    <li class="feature feature--anomaly">
      <svg class="feature-icon" viewBox="0 0 88 88" aria-hidden="true">
        <circle cx="44" cy="44" r="42" fill="var(--orange)" stroke="var(--white)" stroke-width="2"/>
        <g fill="none" stroke="var(--white)" stroke-width="2">
          <rect x="24" y="24" width="40" height="36"/>
          <line x1="24" y1="31" x2="64" y2="31"/>
          <line x1="29" y1="38" x2="40" y2="38"/>
          <line x1="29" y1="44" x2="38" y2="44"/>
          <line x1="29" y1="50" x2="40" y2="50"/>
          <circle cx="51" cy="45" r="8"/>
          <line x1="57" y1="51" x2="64" y2="58"/>
        </g>
      </svg>
      <div class="feature-label">Anomaly Detection</div>
      <div class="feature-rule"></div>
    </li>
    <li class="feature feature--insider">
      <svg class="feature-icon" viewBox="0 0 88 88" aria-hidden="true">
        <circle cx="44" cy="44" r="42" fill="var(--orange)" stroke="var(--white)" stroke-width="2"/>
        <g fill="none" stroke="var(--white)" stroke-width="2">
          <rect x="22" y="24" width="44" height="30"/>
          <line x1="44" y1="54" x2="44" y2="62"/>
          <line x1="34" y1="62" x2="54" y2="62"/>
          <circle cx="40" cy="38" r="9"/>
          <line x1="46" y1="45" x2="60" y2="58"/>
          <circle cx="40" cy="38" r="3"/>
        </g>
      </svg>
      <div class="feature-label">Insider Threat</div>
      <div class="feature-rule"></div>
    </li>
    <li class="feature feature--activity">
      <svg class="feature-icon" viewBox="0 0 88 88" aria-hidden="true">
        <circle cx="44" cy="44" r="42" fill="var(--orange)" stroke="var(--white)" stroke-width="2"/>
        <g fill="none" stroke="var(--white)" stroke-width="2">
          <rect x="24" y="30" width="40" height="26"/>
          <line x1="36" y1="62" x2="52" y2="62"/>
          <rect x="32" y="22" width="18" height="24"/>
          <line x1="36" y1="29" x2="46" y2="29"/>
          <line x1="36" y1="34" x2="44" y2="34"/>
          <circle cx="52" cy="46" r="6"/>
          <line x1="56" y1="50" x2="62" y2="56"/>
        </g>
      </svg>
      <div class="feature-label">User Activity Reviews</div>
      <div class="feature-rule"></div>
    </li>
  </ul>

  <div class="social" aria-label="Social links">
    <span class="social-rule"></span>
    <span class="social-dot social-dot--one"></span>
    <span class="social-dot social-dot--two"></span>
  </div>

  <svg class="footer-shapes" width="960" height="120" viewBox="0 0 960 120" aria-hidden="true">
    <polygon points="360,26 372,26 320,120 307,120" fill="var(--white)"/>
    <polygon points="400,0 960,0 960,120 332,120" fill="var(--orange)"/>
  </svg>

  <p class="web-address">www.<strong>brimoxsecurity</strong>.net</p>

</main>
</body>
</html>
```